New Company Brochure for Email send out

Want to have a new professional and eye catching company brochure
We are an I.T. Infrastructure solution provider

Focus Solution
1) Server Room Setup (UPS, CRAC, etc)
2) All-in-One Rack Solution (Key focus)
3) Structured Cabling and Fiber Backbone wiring
4) other solution (CCTV & Access Control Solution, Conference Room AV Solution)

Hope to have
1) total around 6 pages (including front cover and last page)
2) Suggested format : Powerpoint, word, excel or visio
3) sorry we have no knowledge on AI
Updates

Low design quality

Target Market(s)

Enterprise

Industry/Entity Type

I.T.

Requirements
Must have
• Our Product Photo (All-in-One Rack Solution, Structured Cabling, Server room Setup)
Nice to have
• Some our vendor partners logo
Should not have
• Our Existing Client Logo

```html
<!DOCTYPE html>
<html lang="en">
<head>
<meta charset="utf-8">
<title>Nexa Technology Solutions – Company Brochure</title>
<link href="https://fonts.googleapis.com/css2?family=Saira+Condensed:wght@600;700&family=Roboto:wght@400;500;700&display=swap" rel="stylesheet">
<style>
:root{
  --bg:#eceef1;
  --paper:#ffffff;
  --blue:#1553b4;
  --blue-dark:#0d3f8f;
  --blue-light:#2a8ad8;
  --green:#1aae8c;
  --green-light:#9ad9c6;
  --orange:#ee7d22;
  --yellow:#f6cf5a;
  --pink:#e73552;
  --pink-light:#f28fa3;
  --ink:#1e1e1e;
  --muted:#555;
  --navy:#0b1c3a;
}
*{box-sizing:border-box;margin:0;padding:0}
html,body{width:1200px;height:1000px;overflow:hidden;background:var(--bg);font-family:"Roboto",sans-serif;color:var(--ink)}
.spread{position:relative;width:1200px;height:1000px}
.page{position:absolute;width:326px;height:418px;background:var(--paper);overflow:hidden;box-shadow:0 3px 10px rgba(0,0,0,.14)}
.abs{position:absolute}
.photo{position:absolute}
.photo-dc{background:radial-gradient(ellipse at 55% 55%,#e8f4ff 0,#8cc6f2 14%,#2b66b0 38%,#0d2a5c 70%,#071633 100%)}
.photo-dc-dark{background:radial-gradient(ellipse at 62% 40%,#ffffff 0,#bfe0ff 8%,#2f6cb6 30%,#0e2a57 60%,#061228 100%)}
.photo-rack{background:linear-gradient(90deg,#f7f7f7 0,#3a3d42 6%,#1b1d21 30%,#2a2d33 36%,#1b1d21 64%,#2a2d33 70%,#1b1d21 94%,#f7f7f7 100%)}
.heading{font-family:"Saira Condensed",sans-serif;font-weight:700;color:#fff;text-transform:uppercase;letter-spacing:.3px}
.band-title{position:absolute;left:0;top:29px;height:57px;padding:9px 0 0 20px;font-size:19px;line-height:20px;border-top-right-radius:24px}
.body{font-size:5.1px;line-height:8.2px;color:var(--ink)}
.hl-blue{color:var(--blue);font-weight:500}
.hl-green{color:var(--green);font-weight:500}
.hl-orange{color:var(--orange);font-weight:500}
.brand{display:flex;align-items:center;gap:6px;color:var(--blue);font-family:"Roboto",sans-serif;font-weight:500}
.brand-mark{border:3px solid var(--blue)}
.dots{position:absolute;display:grid;gap:3px}
.dots i{display:block;width:2px;height:2px;background:#9fd8c8}
.partners-label{position:absolute;font-size:6px;color:var(--ink)}
.badge{position:absolute;border-radius:3px}
ul.list{list-style:none}
ul.list li{position:relative;padding-left:5px}
ul.list li::before{content:"•";position:absolute;left:0}
</style>
</head>
<body>
<main class="spread">

  <!-- Cover -->
  <section class="page cover" style="left:55px;top:57px">
    <div class="photo photo-dc" role="img" aria-label="Data center aisle with server racks" style="left:90px;top:27px;width:203px;height:207px;border-top-left-radius:40px"></div>
    <div class="abs" style="left:176px;top:110px;width:150px;height:204px;border:23px solid var(--green);border-right:none"></div>
    <div class="abs" style="left:307px;top:62px;width:19px;height:37px;background:var(--blue)"></div>
    <div class="abs" style="left:120px;top:249px;width:39px;height:34px;background:var(--green)"></div>
    <div class="heading abs" style="left:0;top:151px;width:164px;height:83px;background:linear-gradient(90deg,var(--blue-dark),var(--blue-light));border-top-right-radius:18px;padding:11px 0 0 26px;font-size:17px;line-height:21px">Data Center<br>Infrastructure<br>Solution</div>
    <div class="dots" style="left:53px;top:88px;grid-template-columns:repeat(8,2px)"><i></i><i></i><i></i><i></i><i></i><i></i><i></i><i></i></div>
    <div class="dots" style="left:30px;top:265px;grid-template-columns:repeat(3,2px)"><i></i><i></i><i></i><i></i><i></i><i></i><i></i><i></i><i></i><i></i><i></i><i></i><i></i><i></i><i></i><i></i><i></i><i></i></div>
    <div class="dots" style="left:284px;top:339px;grid-template-columns:repeat(6,2px)"><i></i><i></i><i></i><i></i><i></i><i></i><i></i><i></i><i></i><i></i><i></i><i></i></div>
    <div class="brand abs" style="left:29px;top:362px;font-size:22px"><span class="brand-mark" style="width:26px;height:26px"></span>Nexa</div>
    <div class="abs" style="left:221px;top:376px;font-size:7.5px;letter-spacing:.3px;color:var(--ink)">www.nexatech.example</div>
  </section>

  <!-- Server room -->
  <section class="page server-room" style="left:434px;top:57px">
    <div class="photo photo-dc" role="img" aria-label="Server room with digital light effects" style="left:0;top:0;width:308px;height:86px;border-bottom-right-radius:30px"></div>
    <div class="heading band-title" style="width:164px;background:linear-gradient(90deg,var(--blue-dark),var(--blue))">Server Room<br>Design &amp; Build</div>
    <p class="body abs" style="left:20px;top:99px;width:134px"><span class="hl-blue">Data Center is like a brain to a business</span> deserving and demanding top-level attention and tremendous resources from time to time. All the components contained inside a Data Center are all critical facilities; Backup Power, Ventilating &amp; Air Conditioning, Fire Suppression, Environmental Monitoring, Access Controls, and eventually the most crucial and delicate elements were those server data.<br><br>While most businesses may not have adequate staffing level in IT, human resources will be way overextended when coming across a need in Data Center Expansion, New-build or Refurbishment. In Nexa Technology, you are able to focus your efforts in daily operation duties and rely the design/build process to our very specialised expertise in the market for decades.</p>
    <div class="abs" style="left:187px;top:102px;font-size:7px;font-weight:700;color:var(--ink)">Corvane <span style="font-weight:400;color:#888">|</span> <span style="font-weight:500">Smart Solutions</span></div>
    <svg class="abs" style="left:0;top:210px" width="326" height="208" viewBox="0 0 326 208"><path d="M0 44 H143 C158 44 160 12 178 12 H326 V208 H0 Z" fill="var(--blue)"/></svg>
    <div class="photo photo-rack" role="img" aria-label="Three black UPS cabinets" style="left:170px;top:120px;width:144px;height:126px"></div>
    <div class="abs" style="left:20px;top:271px;font-size:7.2px;line-height:9px;font-weight:500;color:#fff">NEXA's Solution in Data Center<br>Design/Build includes:</div>
    <ul class="list abs" style="left:20px;top:297px;font-size:5.1px;line-height:10.4px;color:#fff">
      <li>Uninterruptable Power Supply (UPS)</li><li>Power Distribution System</li><li>Computer Room Air Conditioning System</li><li>Fire Extinguishing System</li><li>Builder Works (Fire Rated Wall and Door)</li><li>Raised Floor System</li><li>Environmental Monitoring System</li><li>IP-KVM and iPDU</li><li>Enclosed Rack and Open Rack</li><li>Hot/Cold Containment Solution</li>
    </ul>
    <div class="photo" role="img" aria-label="UPS units" style="left:146px;top:276px;width:92px;height:63px;background:linear-gradient(135deg,#fff,#d9dbde 60%,#3b3f45)"></div>
    <div class="photo" role="img" aria-label="Enclosed server rack aisle" style="left:243px;top:276px;width:83px;height:63px;background:linear-gradient(135deg,#c9d9ea,#3a5676 60%,#1d2f45)"></div>
    <div class="photo" role="img" aria-label="Technician working under raised floor" style="left:146px;top:346px;width:57px;height:51px;background:linear-gradient(135deg,#6b5a4e,#2a2f3a)"></div>
    <div class="photo" role="img" aria-label="Fire suppression piping" style="left:207px;top:346px;width:57px;height:51px;background:linear-gradient(135deg,#7e8b63,#3f4a3a)"></div>
    <div class="photo" role="img" aria-label="Power distribution breakers" style="left:268px;top:346px;width:58px;height:51px;background:linear-gradient(135deg,#dfe3e6,#8d98a3)"></div>
  </section>

  <!-- All-in-one rack -->
  <section class="page rack" style="left:812px;top:57px">
    <div class="photo photo-dc-dark" role="img" aria-label="Data center aisle" style="left:0;top:0;width:308px;height:86px;border-bottom-right-radius:30px"></div>
    <div class="heading band-title" style="width:164px;background:linear-gradient(90deg,var(--green),var(--green-light))">All-in-One<br>Rack Solution</div>
    <p class="body abs" style="left:24px;top:103px;width:140px">All-in-one rack enclosure is a new approach of rack providing a <span class="hl-green">self-contained ecosystem</span> to accommodate servers and devices. It itself already contained modular cooling, fire suppression, backup power, PDU, remote monitoring and infrastructure management tool.<br><br>With its pre-configured module, it is a perfect partner to commercials who has little space for their IT device, temp or remote office and who needs speedy deployment. Plus its perfect plug-play design, it can be easily relocated and reinstalled in a new location with only minimal expenses.</p>
    <div class="photo photo-rack" role="img" aria-label="Three all-in-one rack cabinets" style="left:188px;top:97px;width:105px;height:92px"></div>
    <div class="photo photo-dc-dark" role="img" aria-label="Server aisle in data center" style="left:0;top:216px;width:326px;height:144px"></div>
    <div class="photo photo-dc-dark" style="left:174px;top:194px;width:152px;height:30px;border-top-left-radius:14px"></div>
    <div class="dots" style="left:300px;top:160px;grid-template-columns:repeat(3,2px)"><i></i><i></i><i></i><i></i><i></i><i></i><i></i><i></i><i></i><i></i><i></i><i></i></div>
    <div class="heading abs" style="left:26px;top:256px;font-size:14px;line-height:17px">We design, build<br>and maintain<br>your data center<br>as you want it.</div>
    <div class="partners-label" style="left:21px;top:370px">Our Partners</div>
    <div class="badge" style="left:21px;top:381px;width:54px;height:21px;background:var(--orange)"></div>
    <div class="badge" style="left:85px;top:385px;width:36px;height:13px;background:#2b79c6"></div>
    <div class="badge" style="left:131px;top:381px;width:18px;height:21px;background:#c3245e"></div>
    <div class="badge" style="left:164px;top:385px;width:30px;height:13px;background:#d12027"></div>
    <div class="badge" style="left:204px;top:387px;width:52px;height:9px;background:#d23a2b"></div>
    <div class="badge" style="left:266px;top:388px;width:38px;height:7px;background:#9aa3ad"></div>
  </section>

  <!-- Structured cabling -->
  <section class="page cabling" style="left:55px;top:522px">
    <div class="photo" role="img" aria-label="Network cable connectors close-up" style="left:0;top:0;width:308px;height:86px;border-bottom-right-radius:30px;background:linear-gradient(120deg,#6b3fa0,#3d5fb8 45%,#a8c8ea 70%,#5a77b8)"></div>
    <div class="heading band-title" style="width:228px;background:linear-gradient(90deg,var(--orange),var(--yellow));font-size:18px">Structured Cabling<br>&amp; Fiber Backbone Wiring</div>
    <p class="body abs" style="left:20px;top:100px;width:136px">Structured cabling is the design and installation of a cabling systems that will support multiple hardware uses systems and be suitable for today's needs and those of the future. We deliver robust structured cabling systems that are equipped to accommodate a multitude of applications including voice, data, video, security, and etc.<br><br>From the walk through to cable design and installation, we ensure your entire project is completed with <span class="hl-orange">minimal interruption, utilising best practices, delivered on time, and within budget.</span></p>
    <div class="abs" style="left:184px;top:108px;width:26px;height:26px;border-radius:4px;background:var(--orange)"></div>
    <div class="abs" style="left:184px;top:147px;width:26px;height:26px;border-radius:4px;background:var(--orange)"></div>
    <div class="heading abs" style="left:220px;top:110px;font-size:10px;line-height:10.5px;font-weight:600;color:var(--ink);text-transform:none">Make More Meaningful<br>Connections</div>
    <div class="heading abs" style="left:220px;top:155px;font-size:10px;font-weight:600;color:var(--ink);text-transform:none">Professional Design</div>
    <div class="body abs" style="left:20px;top:211px;width:136px;font-weight:700">NEXA's solution in Wired and Wireless Network covers:</div>
    <ul class="list body abs" style="left:20px;top:230px;width:136px">
      <li>Comprehensive Network Architecture Design &amp; Enhancement</li><li>Switches, Routers,</li><li>Wireless LAN (Wi-fi) and Controllers</li><li>Security Appliances</li>
    </ul>
    <div class="body abs" style="left:20px;top:282px;font-weight:700">NEXA's solution in Voice covers:</div>
    <ul class="list body abs" style="left:20px;top:292px">
      <li>IP-Telephony</li><li>Voice Logging System</li><li>Auto Attendance and IVRS</li><li>Call Center System</li>
    </ul>
    <div class="photo" role="img" aria-label="Fiber optic patch cables" style="left:167px;top:206px;width:159px;height:73px;border-top-left-radius:14px;background:linear-gradient(135deg,#4a90c8,#e8d86a 45%,#3a6fa5)"></div>
    <div class="photo" role="img" aria-label="Cloud network illustration" style="left:167px;top:286px;width:77px;height:88px;border-bottom-left-radius:14px;background:radial-gradient(circle at 55% 50%,#8fd0ff,#1f6fc8 45%,#0b2a66)"></div>
    <div class="photo" role="img" aria-label="Patch panel rack with blue cables" style="left:249px;top:286px;width:77px;height:132px;border-top-left-radius:14px;background:linear-gradient(180deg,#2a3340,#1e6fa8 50%,#1a2a3a)"></div>
    <div class="partners-label" style="left:20px;top:345px">Our Partners</div>
    <div class="badge" style="left:21px;top:356px;width:56px;height:12px;background:#111"></div>
    <div class="badge" style="left:89px;top:356px;width:37px;height:15px;background:#3a9d8a"></div>
    <div class="badge" style="left:24px;top:381px;width:44px;height:15px;background:#2d4d8f"></div>
    <div class="badge" style="left:85px;top:381px;width:43px;height:16px;border-radius:8px;background:#2b6cb3"></div>
    <div class="badge" style="left:140px;top:384px;width:44px;height:11px;background:#d3202e"></div>
    <div class="badge" style="left:195px;top:384px;width:44px;height:11px;background:#333"></div>
  </section>

  <!-- Other services -->
  <section class="page services" style="left:434px;top:522px">
    <div class="photo" role="img" aria-label="Hand holding a tablet with digital interface" style="left:0;top:0;width:308px;height:86px;border-bottom-right-radius:30px;background:linear-gradient(120deg,#14203a,#2d5a8c 45%,#86b6d8 70%,#2c4e78)"></div>
    <div class="heading band-title" style="width:132px;background:linear-gradient(90deg,var(--pink),var(--pink-light))">Our Other<br>Service</div>

    <div class="photo" role="img" aria-label="Dome security camera" style="left:25px;top:101px;width:122px;height:84px;background:linear-gradient(135deg,#e6eef5,#b9c9d8 60%,#5d6b7a)"></div>
    <div class="abs" style="left:147px;top:101px;width:158px;height:84px;border:1px solid #e3e3e3;border-left:none;padding:7px 0 0 11px">
      <div style="font-size:8.3px;font-weight:500;margin-bottom:4px">Digital &amp; Video Surveillance</div>
      <ul class="list" style="font-size:5px;line-height:9.3px">
        <li>4 to 64 Channels Digital Surveillance System</li><li>High Resolution IP Camera (Support 4K Resolution)</li><li>PTZ Controllable Camera</li><li>Outdoor Camera with Housing and Bracket</li><li>Support PC software and Brower remote monitoring</li><li>Support iOS /Android APP remote monitoring</li>
      </ul>
    </div>

    <div class="photo" role="img" aria-label="Open hands with digital lock symbol" style="left:25px;top:194px;width:122px;height:83px;background:radial-gradient(circle at 50% 40%,#cfe6ff,#2a5ca8 45%,#0d2350)"></div>
    <div class="abs" style="left:147px;top:194px;width:158px;height:83px;border:1px solid #e3e3e3;border-left:none;padding:10px 0 0 11px">
      <div style="font-size:8.3px;font-weight:500;margin-bottom:4px">Access Control Solution</div>
      <ul class="list" style="font-size:5px;line-height:9.3px">
        <li>Two or more factor authentications</li><li>Card identification</li><li>Password identification</li><li>Fingerprint identification</li><li>Facial identifcation</li>
      </ul>
    </div>

    <div class="photo" role="img" aria-label="Video conference meeting room" style="left:25px;top:286px;width:122px;height:84px;background:linear-gradient(135deg,#e9e6e1,#9a9088 55%,#4a4440)"></div>
    <div class="abs" style="left:147px;top:286px;width:158px;height:84px;border:1px solid #e3e3e3;border-left:none;padding:12px 0 0 11px">
      <div style="font-size:8.3px;font-weight:500;margin-bottom:4px">Audiovisual &amp; Conference Room</div>
      <ul class="list" style="font-size:5px;line-height:9.3px">
        <li>Video Conferencing System</li><li>Telepresence</li><li>Conference Room Centralised Control System</li><li>Interactive Presentation Tools</li>
      </ul>
    </div>

    <div class="partners-label" style="left:25px;top:377px">Our Partners</div>
    <div class="badge" style="left:25px;top:391px;width:58px;height:10px;background:#d3202e"></div>
    <div class="badge" style="left:96px;top:390px;width:42px;height:12px;background:#2b2b2b"></div>
    <div class="badge" style="left:152px;top:391px;width:51px;height:10px;background:#555"></div>
    <div class="badge" style="left:215px;top:389px;width:33px;height:14px;border-radius:7px;background:#d2398a"></div>
  </section>

  <!-- Back cover -->
  <section class="page back" style="left:812px;top:522px">
    <div class="brand abs" style="left:72px;top:78px;font-size:40px;gap:12px"><span class="brand-mark" style="width:52px;height:52px;border-width:5px"></span>Nexa</div>
    <div class="abs" style="left:0;width:326px;top:184px;text-align:center;font-size:8.5px">Global Standard</div>
    <div class="badge" style="left:57px;top:206px;width:48px;height:20px;border-radius:10px;background:#1b3f8f"></div>
    <div class="abs" style="left:40px;top:232px;width:82px;text-align:center;font-size:4.6px;line-height:5.5px"><b>DC Tier Standard</b><br>4 Rating Data Centre</div>
    <div class="badge" style="left:127px;top:210px;width:72px;height:18px;background:#6fb83c"></div>
    <div class="badge" style="left:219px;top:206px;width:48px;height:20px;background:#1f56a8"></div>
    <div class="abs" style="left:203px;top:232px;width:82px;text-align:center;font-size:4.6px;line-height:5.5px"><b>DC Design Practice</b><br>Data Center Design and Implementation Best Practices</div>

    <div class="abs" style="left:0;top:290px;width:253px;height:128px;background:linear-gradient(90deg,var(--blue-dark),var(--blue-light));border-top-right-radius:26px"></div>
    <div class="abs" style="left:162px;top:349px;width:139px;height:69px;border:13px solid var(--green);border-bottom:none"></div>
    <div class="abs" style="left:183px;top:351px;width:36px;height:18px;background:var(--blue-light)"></div>
    <div class="dots" style="left:235px;top:328px;grid-template-columns:repeat(6,2px)"><i></i><i></i><i></i><i></i><i></i><i></i><i></i><i></i><i></i><i></i><i></i><i></i></div>

    <div class="contact abs" style="left:26px;top:309px;color:#fff;font-size:6.3px;line-height:9px">
      <div style="font-weight:700;font-size:7px;margin-bottom:6px">CONTACT US</div>
      <div style="font-weight:500">Nexa Technology Solutions Limited</div>
      <div>12 Harbour Lane, Kwun Tong,<br>Kowloon, Hong Kong.</div>
      <div style="margin-top:6px;display:flex;flex-direction:column;gap:2.4px">
        <span><svg width="6" height="5" viewBox="0 0 6 5"><rect width="6" height="5" fill="#fff"/><path d="M0 0 L3 3 L6 0" stroke="#1553b4" stroke-width=".8" fill="none"/></svg> marketing@nexatech.example</span>
        <span><svg width="6" height="6" viewBox="0 0 6 6"><path d="M1 0 L2.2 0 L2.6 1.6 L1.8 2.3 C2.3 3.3 2.8 3.8 3.7 4.2 L4.4 3.4 L6 3.8 L6 5 C6 5.6 5.5 6 5 6 C2.3 5.8 .2 3.7 0 1 C0 .5 .4 0 1 0Z" fill="#fff"/></svg> +852 3100 2200 / +852 5100 3300</span>
        <span><svg width="6" height="6" viewBox="0 0 6 6"><rect x="1.2" y="0" width="3.6" height="2" fill="#fff"/><rect x="0" y="2" width="6" height="2.6" fill="#fff"/><rect x="1.2" y="4" width="3.6" height="2" fill="#fff"/></svg> +852 3100 4400</span>
        <span><svg width="6" height="6" viewBox="0 0 6 6"><circle cx="3" cy="3" r="2.6" fill="none" stroke="#fff" stroke-width=".7"/><path d="M.4 3 H5.6 M3 .4 C1.6 2 1.6 4 3 5.6 C4.4 4 4.4 2 3 .4" stroke="#fff" stroke-width=".5" fill="none"/></svg> www.nexatech.example</span>
      </div>
    </div>
  </section>

</main>
</body>
</html>
```